The Seeds Beneath Wintermoor Inc.

On one side have the business name. On the other side have contact information. This is an indoor cannabis cultivation business. It’s a new company in Sacramento ca. So we need a logo designed. The company is Called the seeds beneath wintermoor. We grow and distribute marijuana in California. We would like to see designers use the color green and communicate cultivation.

Target Market(s)

Networking

Contact Information for Business Card

Wade Tirrenbek: president
Phone: (916) 555-0173
Email: wade@theseedsbeneathwintermoor.net

Logo Text

Not sure if i want text or just an image created by designers.

Font styles to use
Script

Colors
000000
9bcb3c
fbfcf7
cadf82

Requirements
Nice to have
• A classic elegant professional card.

```html
<!DOCTYPE html>
<html lang="en">
<head>
<meta charset="utf-8">
<title>The Seeds Beneath Wintermoor — Business Card</title>
<link rel="stylesheet" href="https://fonts.googleapis.com/css2?family=Montserrat:wght@500;600&display=swap">
<style>
  :root {
    --backdrop: #8c8c8c;
    --card-black: #161616;
    --mark-on-black: #2f2f2f;
    --card-white: #fbfcf7;
    --leaf-green: #9bcb3c;
    --ink: #2a2a2a;
  }
  * { margin: 0; padding: 0; box-sizing: border-box; }
  html, body { width: 1200px; height: 1171px; overflow: hidden; }
  body {
    position: relative;
    background: var(--backdrop);
    font-family: "Montserrat", Arial, sans-serif;
  }
  .card {
    position: absolute;
    left: 239px;
    width: 681px;
    height: 378px;
  }
  .card--front {
    top: 154px;
    background: var(--card-black);
    display: flex;
    align-items: center;
    justify-content: center;
  }
  .card--back {
    top: 614px;
    background: var(--card-white);
  }
  .wordmark {
    font-weight: 600;
    line-height: 1.05;
    letter-spacing: 0.01em;
  }
  .card--front .wordmark {
    color: var(--mark-on-black);
    font-size: 44px;
    text-align: center;
  }
  .card--back .wordmark {
    position: absolute;
    right: 59px;
    top: 62px;
    color: var(--leaf-green);
    font-size: 30px;
    text-align: right;
  }
  .contact {
    position: absolute;
    left: 59px;
    top: 192px;
    color: var(--ink);
  }
  .contact__name {
    color: var(--leaf-green);
    font-size: 25px;
    font-weight: 600;
    letter-spacing: 0.02em;
  }
  .contact__role {
    font-size: 18px;
    font-weight: 500;
    margin-top: 2px;
  }
  .contact__rule {
    width: 20px;
    height: 2px;
    background: var(--ink);
    margin: 15px 0 14px;
  }
  .contact__line {
    display: flex;
    align-items: center;
    gap: 8px;
    font-size: 18px;
    font-weight: 500;
    line-height: 25px;
  }
  .contact__icon { width: 19px; height: 15px; flex: none; }
</style>
</head>
<body>
  <section class="card card--front">
    <p class="wordmark">The Seeds<br>Beneath Wintermoor</p>
  </section>

  <section class="card card--back">
    <p class="wordmark">The Seeds<br>Beneath Wintermoor</p>
    <div class="contact">
      <p class="contact__name">Wade Tirrenbek</p>
      <p class="contact__role">President</p>
      <div class="contact__rule"></div>
      <p class="contact__line">
        <svg class="contact__icon" viewBox="0 0 19 15" aria-hidden="true">
          <path fill="#9bcb3c" d="M1 5c0-3 17-3 17 0v1.5h-4V5H5v1.5H1z"/>
          <path fill="#9bcb3c" d="M5 7h9l3 7H2z"/>
          <circle cx="9.5" cy="10.5" r="2" fill="#fbfcf7"/>
        </svg>
        (916) 555-0173
      </p>
      <p class="contact__line">
        <svg class="contact__icon" viewBox="0 0 19 15" aria-hidden="true">
          <rect x="0.5" y="1.5" width="18" height="12" fill="#9bcb3c"/>
          <path d="M1 2l8.5 7L18 2M1 13l6-5M18 13l-6-5" stroke="#fbfcf7" stroke-width="1.2" fill="none"/>
        </svg>
        wade@theseedsbeneathwintermoor.net
      </p>
    </div>
  </section>
</body>
</html>
```